Re-Design Business Card and Logo for Plastic Printing

Business is a small financial planning (investments, insurance, retirement, etc.) firm. The majority of our clients are 55+ years old, professional occupations (pilots, doctors, bankers, etc.) but not necessarily "high net worth."
I would like to have a design that would be used on clear plastic business cards. I have found a vendor that makes these but I do not have the ability to design these like I want.
I do have one proof but I just don't feel like it's the right one for me. Also, I feel that I need some help with a logo redesign so maybe someone could handle that for me as well.
I want the final design to "eye catching" but still be tasteful. I am open to suggestion regarding colors and such.
I will include the old design as well as the new proof I have to give you an idea of what I current have. Keep in mind, I have no allegiance to the attached designs.
For the second file (Business Card New Proof), the white space shown will be transparent when printed on plastic card.
Target Market(s)
Mostly people age 55+ in professional occupations.
Industry/Entity Type
Financial Service
Contact Information for Business Card
Looking for design that can be printed on clear plastic cards (if possible).
Logo Text
KFG - Kestwick Finance Group
Requirements
Must have
- Must be double sided because disclosure is required for compliance reasons.
Designations (must include the Registered trademark symbol as follows)...
MBA, ChFC®, CLU®, CRPS®
Nice to have
- The little icons next to email, phone and fax are nice.
Should not have
- I think I would like to eliminate the Owner and Co-Founder line that you see on the attachments.

```html
<!DOCTYPE html>
<html lang="en">
<head>
<meta charset="utf-8">
<title>Kestwick Finance Group – Business Card</title>
<link rel="stylesheet" href="https://fonts.googleapis.com/css2?family=Open+Sans:wght@400;600;700&family=Montserrat:wght@500&display=swap">
<style>
  :root {
    --stage: #1f1f21;
    --card-sky: #86add6;
    --card-navy: #11416e;
    --card-slate: #5b5e63;
    --ink-white: #ffffff;
    --icon-grey: #c9d3de;
  }
  * { box-sizing: border-box; margin: 0; padding: 0; }
  html, body { width: 1200px; height: 791px; overflow: hidden; }
  body {
    background: var(--stage);
    font-family: "Open Sans", Arial, sans-serif;
    display: flex; align-items: center; justify-content: center; gap: 40px;
  }
  .card {
    position: relative; width: 560px; height: 320px;
    border-radius: 26px; overflow: hidden; background: var(--card-sky);
  }
  .card-art { position: absolute; inset: 0; width: 100%; height: 100%; }
  .brand {
    position: absolute; display: flex; align-items: center; gap: 10px;
    color: var(--card-navy); font-weight: 700; text-transform: uppercase;
    line-height: 1.05; letter-spacing: .02em;
  }
  .brand-mark { width: 22px; height: 22px; background: var(--card-navy); flex: none; }
  .front .brand { left: 150px; top: 92px; font-size: 20px; }
  .back .brand { left: 40px; top: 218px; font-size: 18px; }
  .brand-name span { display: block; }
  .disclosure {
    position: absolute; left: 60px; right: 60px; bottom: 26px;
    color: var(--ink-white); font-size: 7.5px; line-height: 1.45; text-align: center;
  }
  .contact {
    position: absolute; right: 74px; top: 58px; text-align: right;
    color: var(--ink-white); font-size: 12.5px; line-height: 1.35;
  }
  .contact-name { font-family: "Montserrat", Arial, sans-serif; font-size: 19px; font-weight: 500; }
  .contact-titles { font-size: 8.5px; letter-spacing: .03em; margin-bottom: 12px; }
  .contact-address { margin-bottom: 14px; }
  .contact-line { margin-bottom: 14px; }
  .icon-rail {
    position: absolute; right: 0; top: 0; bottom: 0; width: 52px;
    background: var(--card-navy);
    display: flex; flex-direction: column; align-items: center; gap: 30px; padding-top: 46px;
  }
  .icon-rail svg { width: 16px; height: 16px; fill: var(--icon-grey); }
</style>
</head>
<body>

<section class="card front" aria-label="Card front with disclosure">
  <svg class="card-art" viewBox="0 0 560 320" aria-hidden="true">
    <path d="M0,236 C140,214 250,178 360,148 C450,124 520,96 560,56 L560,320 L0,320 Z" fill="var(--card-navy)"/>
    <path d="M150,222 C250,176 360,132 470,112 C420,150 320,190 150,222 Z" fill="var(--card-slate)"/>
    <path d="M0,236 C140,214 250,178 360,148 C450,124 520,96 560,56" fill="none" stroke="var(--ink-white)" stroke-width="1.3"/>
  </svg>
  <div class="brand">
    <div class="brand-mark"></div>
    <div class="brand-name"><span>KFG · Kestwick</span><span>Finance Group</span></div>
  </div>
  <p class="disclosure">Owen Marlow is a registered representative of and offers securities and advisory services through Harbor Crest Securities Corporation. Member Investor Shield Fund. Harbor Crest Securities Corporation is a member of the Harbor Crest Group, which is the marketing name for Harbor Crest National Corporation and its affiliates.</p>
</section>

<section class="card back" aria-label="Card back with contact details">
  <svg class="card-art" viewBox="0 0 560 320" aria-hidden="true">
    <path d="M240,0 C300,90 300,210 345,320" fill="none" stroke="var(--ink-white)" stroke-width="1.3"/>
  </svg>
  <div class="brand">
    <div class="brand-mark"></div>
    <div class="brand-name"><span>KFG · Kestwick</span><span>Finance Group</span></div>
  </div>
  <div class="contact">
    <p class="contact-name">Owen Marlow</p>
    <p class="contact-titles">MBA, ChFC®, CLU®</p>
    <p class="contact-address">2170 Harlan Rd<br>Suite 310<br>Brookfield, VA 23510</p>
    <p class="contact-line">(555) 014-2287</p>
    <p class="contact-line">omarlow@kestwickfg.com</p>
    <p class="contact-line">Toll Free (555) 019-4630</p>
  </div>
  <div class="icon-rail" aria-hidden="true">
    <svg viewBox="0 0 16 16"><circle cx="8" cy="5" r="3.2"/><path d="M2 15c0-3.5 2.7-5.5 6-5.5s6 2 6 5.5z"/></svg>
    <svg viewBox="0 0 16 16"><path d="M8 1a5 5 0 0 0-5 5c0 3.8 5 9 5 9s5-5.2 5-9a5 5 0 0 0-5-5zm0 7a2 2 0 1 1 0-4 2 2 0 0 1 0 4z"/></svg>
    <svg viewBox="0 0 16 16"><path d="M4 1.5l2.3 3-1.4 1.6c.8 1.8 2.2 3.2 4 4l1.6-1.4 3 2.3-1.2 2.5C7 13.5 2.5 9 2 2.7z"/></svg>
    <svg viewBox="0 0 16 16"><path d="M1 3h14v10H1zm1.5 1.2V5l5.5 4 5.5-4v-.8z"/></svg>
    <svg viewBox="0 0 16 16"><path d="M4 1h8v4H4zM1 6h14v6h-3v3H4v-3H1zm4 4v4h6v-4z"/></svg>
  </div>
</section>

</body>
</html>
```